WTF!!! We need a modern professional website for a business litigation law firm.

We need a modern, clean, professional and uncomplicated website for a new business trial and litigation law firm called "Harrowgate Trial Firm PLLC". Website must be mobile optimized for iPad and smartphone. The law firm specializes in counseling and representing large corporations, small businesses and entrepreneurs in and out of the courtroom. Lawyers in the firm serve as Florida counsel and trial counsel to organizations facing claims involving product liability, premises liability, professional liability, vehicle and transportation liability, warranty claims, construction defects and delay claims, complex business disputes, commercial litigation and bid disputes in State and Federal Courts. The website is mainly to provide information about the firm, and should include sections describing the firm, identifying the Industries Served and Areas of Practice ," a separate page identifying the "Professionals", a separate page for "Resources & Advisories," and a traveling "Connect With Us" button a site visitor can click on that will launch an email to the Firm's general email account. The website should allow us to easily modify the content on these pages, and let us add/modify links to external information sources. We will not sell anything or take payments through the website. We do need to be able to easily upload and update photographs of attorneys and add new attorneys names/email hyperlinks as the firm grows. We would like to add developments in the law or success stories easily and quickly, such as through a blog page. On the "Connect With Us" page the website should have hyperlinks to email the Firm, and there should be hyperlinks to email each professional on the "Professionals" page. The website should be viewable on mobile devices without distortion. The law firm focuses on trial work and should have some imagery associated with courtrooms, but the overall theme of the site should be modern, clean, and communicate sophistication and strength. The website should be made in Wordpress. We have uploaded logo files for Harrowgate Trial Firm.

Target Market(s)

Corporations and companies that are looking for legal representation. Other attorneys/legal industry.

Industry/Entity Type

Legal Industry

Coding

Coded - Design and coding required

Number of Pages Required

1 page

Font styles to use
Sans Serif

Requirements
Must have
• Simple, clean, sophisticated, modern website that includes the logo, watermark of logo, and the elements described above.
Nice to have
• Pictures of city scape, buildings, courtroom, team members.

```html
<!DOCTYPE html>
<html lang="en">
<head>
<meta charset="utf-8">
<title>Harrowgate Trial Firm</title>
<link href="https://fonts.googleapis.com/css2?family=Montserrat:ital,wght@0,400;0,500;0,600;0,700;0,800;1,400&display=swap" rel="stylesheet">
<style>
:root{
  --blue:#1a86e6;
  --blue-dark:#0f6fc4;
  --black:#000;
  --ink:#111;
  --text:#2a2a2a;
  --muted:#555;
  --white:#fff;
  --card-dark:#0b0b0b;
  --line:#d8d8d8;
}
*{margin:0;padding:0;box-sizing:border-box}
html,body{width:1200px;height:5008px;overflow:hidden}
body{font-family:'Montserrat',sans-serif;color:var(--text);background:var(--white);position:relative}
section,header,footer{position:absolute;left:0;width:1200px}
.abs{position:absolute}
.photo{position:absolute}
.eyebrow{color:var(--blue);font-size:17px;font-weight:500;text-transform:uppercase;letter-spacing:.3px}
.title{font-weight:800;text-transform:uppercase;color:var(--ink);letter-spacing:.5px}
.btn{position:absolute;display:flex;align-items:center;justify-content:center;background:var(--blue);color:var(--white);font-size:12px;font-weight:600;letter-spacing:1px;text-transform:uppercase;text-decoration:none}
.btn::after{content:"";position:absolute;left:18px;right:18px;bottom:-8px;height:2px;background:var(--blue)}
.center{left:0;width:1200px;text-align:center}

/* hero */
.hero{top:0;height:1231px;background:var(--black)}
.hero-photo{top:0;left:0;width:1200px;height:600px;background:linear-gradient(180deg,rgba(70,70,95,.9) 0%,rgba(120,95,95,.85) 30%,rgba(70,55,50,.85) 65%,#000 100%),linear-gradient(90deg,#5a4a50,#8a7a70 60%,#6e7a8a)}
.brand{left:142px;top:22px;color:var(--white);font-weight:800;text-align:center;line-height:1}
.brand .mark{display:block;width:44px;height:30px;margin:0 auto 6px;border:3px solid var(--white)}
.brand .name{font-size:21px;letter-spacing:.5px}
.brand .sub{font-size:9px;letter-spacing:2px;margin-top:3px}
.contact{display:flex;align-items:center;gap:10px;color:var(--white);font-size:12px;font-weight:600;line-height:1.25}
.contact .ico{width:34px;height:34px;border:1.5px solid var(--white);display:flex;align-items:center;justify-content:center}
.contact small{display:block;font-size:11px;font-weight:500}
.rule{left:443px;top:106px;width:615px;height:1px;background:rgba(255,255,255,.35)}
.nav{top:122px;left:161px;display:flex;gap:0;font-size:11.5px;font-weight:600;color:var(--white);text-transform:uppercase}
.nav a{color:var(--white);text-decoration:none;position:absolute;white-space:nowrap}
.nav a.active{color:var(--blue)}
.hero h1{left:142px;top:215px;font-size:40px;line-height:51px;font-weight:800;color:var(--white);text-transform:uppercase;letter-spacing:.5px}
.hero .lead{left:142px;top:380px;font-size:19px;color:var(--white)}

/* about */
.about-img1{left:99px;top:669px;width:290px;height:220px;background:linear-gradient(135deg,#b9a27e,#6a5a4a 55%,#3a4660)}
.about-img2{left:410px;top:731px;width:232px;height:278px;background:linear-gradient(160deg,#4a3b30,#c9b8a4 55%,#2a2420)}
.about-img3{left:233px;top:819px;width:267px;height:327px;background:linear-gradient(180deg,#d9d6cf,#8a8e94 50%,#2c4a7a);border:6px solid var(--black)}
.about-text{left:694px;top:708px;width:370px}
.about-text h2{font-size:33px;color:var(--white);margin-top:6px}
.about-text h3{font-size:16px;color:var(--white);font-weight:500;letter-spacing:1px;margin-top:2px}
.about-text p{color:var(--white);font-size:12.5px;line-height:22px;margin-top:18px}

/* practice */
.practice{top:1231px;height:1041px;background:var(--white)}
.card{position:absolute;width:294px;height:329px;overflow:hidden}
.card .label{position:absolute;left:20px;right:20px;bottom:22px;display:flex;justify-content:space-between;align-items:center;color:var(--white);font-size:15.5px;font-weight:700;text-transform:uppercase}
.card .shade{position:absolute;inset:0;background:linear-gradient(180deg,rgba(0,0,0,0) 45%,rgba(0,0,0,.75))}
.card.feature{background:var(--card-dark);padding:8px}
.card.feature .inner{border:1.5px solid var(--blue);height:100%;padding:50px 20px 0}
.card.feature h4{color:var(--white);font-size:16px;font-weight:700;text-transform:uppercase}
.card.feature p{color:#d6d6d6;font-size:12px;line-height:22px;margin-top:12px}
.card.feature .more{display:inline-block;color:var(--blue);font-size:11.5px;font-weight:600;margin-top:14px;text-transform:uppercase}

/* industries */
.industries{top:2272px;height:579px;background:linear-gradient(180deg,rgba(20,24,32,.92),rgba(28,34,44,.9)),linear-gradient(120deg,#3a3f48,#1a1c20 60%,#4a4a4a)}
.ind-card{position:absolute;top:175px;width:294px;height:311px;background:var(--black);text-align:center;padding-top:38px;color:var(--white)}
.ind-card h4{font-size:17.5px;font-weight:700;text-transform:uppercase;margin-top:20px}
.ind-card p{font-size:12.5px;line-height:22px;color:#d8d8d8;padding:0 28px;margin-top:10px}
.ind-card svg.go{margin-top:18px}

/* blog */
.blog{top:2851px;height:806px;background:var(--white)}
.meta{font-size:13px;color:var(--ink);text-transform:uppercase}
.meta span{margin:0 10px}
.post-title{font-size:15.5px;font-weight:700;color:var(--ink);line-height:24px}
.more-link{color:var(--blue);font-size:12px;font-weight:600;text-transform:uppercase;display:flex;align-items:center;gap:5px}
.side-post{position:absolute;left:626px;width:432px;height:132px}
.side-post .txt{position:absolute;left:0;top:10px;width:210px}
.side-post .thumb{position:absolute;right:0;top:0;width:212px;height:132px}

/* cta */
.cta{top:3657px;height:466px;background:linear-gradient(180deg,rgba(35,38,44,.82),rgba(25,28,34,.85)),linear-gradient(110deg,#6a6a6a,#9a9a9a 50%,#5a5a5a)}
.cta h2{top:122px;font-size:40px;line-height:51px;color:var(--white)}
.cta p{top:230px;font-size:17px;line-height:29px;color:var(--white);padding:0 250px}

/* testimonials */
.reviews{top:4123px;height:516px;background:var(--white)}
.avatars{left:142px;top:333px;display:flex}
.avatars i{width:36px;height:36px;border-radius:50%;border:2px solid var(--white);background:linear-gradient(160deg,#c9a58a,#6a4e40);margin-right:-8px}
.quote-card{left:554px;top:117px;width:483px;height:304px;background:var(--white);box-shadow:0 4px 24px rgba(0,0,0,.12);padding:58px 40px 0 38px}
.quote-card p{font-size:12.5px;line-height:23px;color:var(--text)}
.quote-badge{left:590px;top:90px;width:54px;height:54px;border-radius:50%;background:var(--blue);display:flex;align-items:center;justify-content:center}
.slider-arrow{width:24px;height:24px;border-radius:50%;display:flex;align-items:center;justify-content:center}

/* footer */
.footer{top:4639px;height:369px;background:var(--black);color:var(--white)}
.footer h5{font-size:14.5px;font-weight:700;text-transform:uppercase;position:relative}
.footer h5::after{content:"";position:absolute;left:0;top:26px;width:34px;height:3px;background:var(--blue)}
.footer ul{list-style:none;font-size:12.5px;line-height:28px;margin-top:32px}
.f-item{display:flex;gap:10px;font-size:12.5px;line-height:18px}
.f-item b{font-weight:600;display:block}
.social li{display:flex;align-items:center;gap:8px;margin-bottom:11px;line-height:22px}
.social i{width:27px;height:27px;border-radius:50%;border:1.5px solid var(--white);display:inline-block}
.f-brand{left:856px;top:100px;width:204px;text-align:center;font-weight:800;line-height:1}
.f-brand .mark{display:block;width:70px;height:50px;border:4px solid var(--white);margin:0 auto 10px}
.f-brand .name{font-size:33px;letter-spacing:.5px}
.f-brand .sub{font-size:17px;letter-spacing:4px;margin-top:4px}
.copyright{left:0;top:317px;width:1200px;height:52px;background:var(--blue);color:var(--white);font-size:12px;display:flex;align-items:center;justify-content:center}
</style>
</head>
<body>

<!-- HERO + ABOUT -->
<section class="hero">
  <div class="photo hero-photo" role="img" aria-label="City skyline with government tower at dusk"></div>

  <div class="abs brand">
    <span class="mark"></span>
    <div class="name">HARROWGATE</div>
    <div class="sub">TRIAL FIRM</div>
  </div>

  <div class="abs contact" style="left:443px;top:31px">
    <span class="ico"><svg width="16" height="16" viewBox="0 0 24 24" fill="#fff"><path d="M6.6 10.8a15 15 0 0 0 6.6 6.6l2.2-2.2a1 1 0 0 1 1-.25 11.4 11.4 0 0 0 3.6.57 1 1 0 0 1 1 1V20a1 1 0 0 1-1 1A17 17 0 0 1 3 4a1 1 0 0 1 1-1h3.5a1 1 0 0 1 1 1c0 1.25.2 2.45.57 3.57a1 1 0 0 1-.25 1z"/></svg></span>
    <div><small>PHONE</small>123-456-7890</div>
  </div>
  <div class="abs contact" style="left:615px;top:31px">
    <span class="ico"><svg width="16" height="14" viewBox="0 0 24 20" fill="none" stroke="#fff" stroke-width="2"><rect x="1" y="1" width="22" height="18"/><path d="M1 1l11 9 11-9"/></svg></span>
    <div><small>EMAIL</small>info@harrowgatetrialfirm.com</div>
  </div>
  <a class="btn" style="left:891px;top:29px;width:167px;height:41px;font-size:11.5px">Connect With Us</a>

  <div class="abs rule"></div>
  <nav class="abs nav" style="left:0;top:122px">
    <a class="active" style="left:161px">Home</a>
    <a style="left:249px">About Us</a>
    <a style="left:363px">Professionals</a>
    <a style="left:516px">Industries Served</a>
    <a style="left:692px">Areas of Practice</a>
    <a style="left:871px">Resources &amp; Advisories</a>
  </nav>
  <div class="abs" style="left:161px;top:140px;width:38px;height:2px;background:var(--blue)"></div>

  <h1 class="abs">Your Trusted<br>Partner in Business<br>Litigation</h1>
  <p class="abs lead">Expert Counsel for Corporations and Entrepreneurs.</p>
  <a class="btn" style="left:142px;top:434px;width:140px;height:44px">Learn More</a>

  <div class="photo about-img1" role="img" aria-label="Looking up at skyscrapers with flags"></div>
  <div class="photo about-img2" role="img" aria-label="Hands signing a document with a pen"></div>
  <div class="photo about-img3" role="img" aria-label="Attorney standing with arms crossed in an office"></div>

  <div class="abs about-text">
    <div class="eyebrow">Who We Are</div>
    <h2 class="title">About Harrowgate</h2>
    <h3>TRIAL FIRM</h3>
    <p>Lorem ipsum dolor sit amet, consectetuer adipicing elit sed diam nonummy nibh euismod tincidunt ut.</p>
    <p style="margin-top:14px">Ut wisi enim ad minim veniam, quis nostru ullamcorper suscipit lobortis nisl ut aliquip ex ea commodo conuat. Duis autem vel eum iriure dolor in henrerit in vulputate velit esse molestie consequat, vel illum dolore eu feugiat nulla facilisis at vero eros et accsan et iusto odio. Lorem ipsum dolor sit amet, consectetuer picing.</p>
  </div>
  <a class="btn" style="left:692px;top:1043px;width:142px;height:44px">Learn More</a>
</section>

<!-- AREAS OF PRACTICE -->
<section class="practice">
  <div class="abs center eyebrow" style="top:88px">Who We Serve</div>
  <h2 class="abs center title" style="top:114px;font-size:31px">Areas of Practice</h2>

  <div class="card" style="left:142px;top:183px;background:linear-gradient(160deg,#3a3a3c,#8a8478 55%,#2a2a2a)" role="img" aria-label="Person writing notes at a desk">
    <div class="shade"></div>
    <div class="label">Product Liability <svg width="18" height="14" viewBox="0 0 18 14" fill="none" stroke="#fff" stroke-width="1.6"><path d="M0 7h16M10 1l6 6-6 6"/></svg></div>
  </div>
  <div class="card feature" style="left:453px;top:183px">
    <div class="inner">
      <h4>Professional Liability</h4>
      <p>Ut wisi enim ad inim iam quis nostru ullamcorper suscipit lis nisl ut aliquip ex ea commodo conuat. Duis autem vel eum iriure dolor rerit in vulputate velit esse molestie conseat, vel illum dolore eu feugiat nulla.</p>
      <span class="more">Learn More &rarr;</span>
    </div>
  </div>
  <div class="card" style="left:764px;top:183px;background:linear-gradient(150deg,#6a4a2a,#2c3040 50%,#4a3a2a)" role="img" aria-label="Law book titled premises liability on a shelf">
    <div class="shade"></div>
    <div class="label">Premises Liability <svg width="18" height="14" viewBox="0 0 18 14" fill="none" stroke="#fff" stroke-width="1.6"><path d="M0 7h16M10 1l6 6-6 6"/></svg></div>
  </div>

  <div class="card" style="left:142px;top:531px;background:linear-gradient(160deg,#8a6a4a,#c9b8a0 50%,#3a3a3a)" role="img" aria-label="Hands reviewing a contract beside a laptop">
    <div class="shade"></div>
    <div class="label">Warranty Claims <svg width="18" height="14" viewBox="0 0 18 14" fill="none" stroke="#fff" stroke-width="1.6"><path d="M0 7h16M10 1l6 6-6 6"/></svg></div>
  </div>
  <div class="card" style="left:453px;top:531px;background:linear-gradient(160deg,#2a2a30,#8a8a90 50%,#3a3020)" role="img" aria-label="Handshake over a desk with scales of justice">
    <div class="shade"></div>
    <div class="label">Commercial Litigation <svg width="18" height="14" viewBox="0 0 18 14" fill="none" stroke="#fff" stroke-width="1.6"><path d="M0 7h16M10 1l6 6-6 6"/></svg></div>
  </div>
  <div class="card" style="left:764px;top:531px;background:linear-gradient(160deg,#d8d4cc,#9a8a78 45%,#4a2a18)" role="img" aria-label="Gavel resting on legal documents">
    <div class="shade"></div>
    <div class="label">Bid Disputes <svg width="18" height="14" viewBox="0 0 18 14" fill="none" stroke="#fff" stroke-width="1.6"><path d="M0 7h16M10 1l6 6-6 6"/></svg></div>
  </div>

  <a class="btn" style="left:475px;top:897px;width:250px;height:45px">View More Practice Areas</a>
</section>

<!-- INDUSTRIES -->
<section class="industries" role="img" aria-label="Dimmed meeting table with glass and documents">
  <div class="abs center eyebrow" style="top:90px">We Specialize In</div>
  <h2 class="abs center title" style="top:116px;font-size:31px;color:var(--white)">Industries We Served</h2>

  <div class="ind-card" style="left:142px">
    <svg width="70" height="70" viewBox="0 0 70 70" fill="none" stroke="var(--blue)" stroke-width="2.5"><path d="M36 66V6h8v60M36 14h30M44 14l8-8 8 8M60 14v14M57 28h6v6h-6zM6 66V44h14v22M20 66V52h14v14M10 50h6M10 56h6M24 58h6M2 66h66"/></svg>
    <h4>Construction</h4>
    <p>Ut wisi enim ad minim veniam, quis nostru ullamcorper suscipit lobortis nisl ut aliquip ex ea commodo.</p>
    <svg class="go" width="38" height="38" viewBox="0 0 38 38" fill="none" stroke="#fff" stroke-width="1.6"><circle cx="19" cy="19" r="16"/><path d="M10 19h18M22 13l6 6-6 6"/></svg>
  </div>
  <div class="ind-card" style="left:453px">
    <svg width="70" height="70" viewBox="0 0 70 70" fill="none" stroke="var(--blue)" stroke-width="2.5"><rect x="14" y="6" width="42" height="52" rx="6"/><path d="M14 30h42M20 14h30v16H20zM22 40h6M42 40h6M20 58v6h8v-6M42 58v6h8v-6M10 18v10M60 18v10M26 48h18"/></svg>
    <h4>Transportation</h4>
    <p>Ut wisi enim ad minim veniam, quis nostru ullamcorper suscipit lobortis nisl ut aliquip ex ea commodo.</p>
    <svg class="go" width="38" height="38" viewBox="0 0 38 38" fill="none" stroke="#fff" stroke-width="1.6"><circle cx="19" cy="19" r="16"/><path d="M10 19h18M22 13l6 6-6 6"/></svg>
  </div>
  <div class="ind-card" style="left:764px">
    <svg width="70" height="70" viewBox="0 0 70 70" fill="none" stroke="var(--blue)" stroke-width="2.5"><path d="M12 6h46l8 18H4zM4 24c0 5 4 8 8 8s8-3 8-8c0 5 4 8 8 8s8-3 8-8c0 5 4 8 8 8s8-3 8-8c0 5 4 8 8 8s8-3 8-8M8 32v32h54V32M16 64V42h14v22M38 42h18v12H38zM4 64h62"/></svg>
    <h4>Retail</h4>
    <p>Ut wisi enim ad minim veniam, quis nostru ullamcorper suscipit lobortis nisl ut aliquip ex ea commodo.</p>
    <svg class="go" width="38" height="38" viewBox="0 0 38 38" fill="none" stroke="#fff" stroke-width="1.6"><circle cx="19" cy="19" r="16"/><path d="M10 19h18M22 13l6 6-6 6"/></svg>
  </div>
</section>

<!-- BLOG -->
<section class="blog">
  <div class="abs center eyebrow" style="top:90px">Articles</div>
  <h2 class="abs center title" style="top:116px;font-size:31px">Latest Blog Posts</h2>

  <div class="photo" style="left:142px;top:183px;width:445px;height:282px;background:linear-gradient(140deg,#d8dce2,#8a9aae 40%,#3a4a6a 70%,#c8c0b4)" role="img" aria-label="Three colleagues meeting around a laptop"></div>
  <div class="abs" style="left:142px;top:496px;width:445px">
    <div class="meta">Excepteur Sint<span>I</span>Jan 2025</div>
    <div class="post-title" style="margin-top:14px">Ut Enim Ad Minim Veniam Quis Nostrud</div>
    <p style="font-size:12px;line-height:19px;color:var(--muted);margin-top:6px">Excepteur sint occaecat cupidatat non proident, sunt in culpa qui officia deserunt mollit anim id est laborum.</p>
    <div class="more-link" style="margin-top:10px">Learn More &rarr;</div>
  </div>

  <div class="side-post" style="top:183px">
    <div class="txt">
      <div class="meta" style="font-size:12px">Excepteur Sint<span>I</span>Jan 2025</div>
      <div class="post-title" style="margin-top:10px">Ut Enim Ad Mini Veiam Quis Nostrud</div>
      <div class="more-link" style="margin-top:10px">Learn More &rarr;</div>
    </div>
    <div class="thumb" style="background:linear-gradient(150deg,#3a2a1a,#9a8a6a 50%,#5a4a38)" role="img" aria-label="Scales of justice on a wooden desk"></div>
  </div>
  <div class="side-post" style="top:337px">
    <div class="txt">
      <div class="meta" style="font-size:12px">Excepteur Sint<span>I</span>Jan 2025</div>
      <div class="post-title" style="margin-top:10px">Ut Enim Ad Mini Veiam Quis Nostrud</div>
      <div class="more-link" style="margin-top:10px">Learn More &rarr;</div>
    </div>
    <div class="thumb" style="background:linear-gradient(150deg,#e8e4dc,#b8a894 50%,#7a6a5a)" role="img" aria-label="Woman working on a laptop in an office"></div>
  </div>
  <div class="side-post" style="top:490px">
    <div class="txt">
      <div class="meta" style="font-size:12px">Excepteur Sint<span>I</span>Jan 2025</div>
      <div class="post-title" style="margin-top:10px">Ut Enim Ad Mini Veiam Quis Nostrud</div>
      <div class="more-link" style="margin-top:10px">Learn More &rarr;</div>
    </div>
    <div class="thumb" style="background:linear-gradient(150deg,#4a4a4e,#9a9aa0 50%,#6a5030)" role="img" aria-label="Handshake beside a gavel"></div>
  </div>

  <a class="btn" style="left:510px;top:664px;width:180px;height:46px">View More Posts</a>
</section>

<!-- CTA -->
<section class="cta" role="img" aria-label="Hands signing paperwork on a desk, dimmed">
  <h2 class="abs center title" style="color:var(--white)">Your Trusted Partner in<br>Business Litigation</h2>
  <p class="abs center">Ut wisi enim ad minim veniam, quis nostru ullamcorper suscipit lobortis nisl ut aliquip ex ea commodo conuat. Duis autem vel eum iriure dolor.</p>
  <a class="btn" style="left:506px;top:299px;width:188px;height:47px">Contact Us Today</a>
</section>

<!-- TESTIMONIALS -->
<section class="reviews">
  <div class="abs eyebrow" style="left:142px;top:150px">Testimonials</div>
  <h2 class="abs title" style="left:142px;top:178px;font-size:32px">Client Reviews</h2>
  <p class="abs" style="left:142px;top:222px;width:350px;font-size:12.5px;line-height:21px">Ut wisi enim ad minim venia quis nostr ullamcorper suscipit lobortis nisl ut aliquip ex ea coodo conuat. Duis autem vel eum iriure dolor in herit in vulputate velit esse molestie consequat vel illum.</p>
  <div class="abs avatars" role="img" aria-label="Client portrait thumbnails"><i></i><i></i><i></i><i style="margin-right:0"></i></div>
  <div class="abs" style="left:142px;top:383px;font-size:12.5px;display:flex;align-items:center;gap:6px">
    <svg width="14" height="14" viewBox="0 0 24 24" fill="#f2b31b"><path d="M12 2l3 7 7 .6-5.3 4.7 1.6 7.2L12 17.8 5.7 21.5l1.6-7.2L2 9.6 9 9z"/></svg>
    <b>5.0</b> (10k Reviews)
  </div>

  <div class="abs quote-card">
    <p>Ut wisi enim ad minim veniam, quis nostru ullamcorp suscipit lobortis nisl ut aliquip ex ea commodo conuat. Duis auem vel eum iriure dolor in henrrit in vuate velit esse motie consequat, vel illum dolore eu feugiat nulla facilisis at vero eros et accsan et iusto odio. Lorem ipsum dolor sit amet consctetuer picing. Lorem ipsum dolor sit amet, consectetuer.</p>
    <div style="display:flex;align-items:center;gap:16px;margin-top:22px">
      <div style="width:54px;height:54px;border-radius:50%;background:linear-gradient(160deg,#c8a890,#4a3a34)" role="img" aria-label="Client portrait"></div>
      <div><div style="font-size:13px;font-weight:700;color:var(--ink)">DANIEL M.</div><div style="font-size:12px;font-style:italic;margin-top:4px">Lorem Ipsum</div></div>
    </div>
  </div>
  <div class="abs quote-badge"><svg width="26" height="22" viewBox="0 0 26 22" fill="#fff"><path d="M0 22V12C0 5 4 1 10 0v4c-3 1-5 3-5 7h5v11zM15 22V12c0-7 4-11 10-12v4c-3 1-5 3-5 7h5v11z"/></svg></div>
  <div class="abs slider-arrow" style="left:538px;top:265px;background:#c8c8c8"><svg width="8" height="10" viewBox="0 0 8 10" fill="none" stroke="#fff" stroke-width="1.6"><path d="M6 1L2 5l4 4"/></svg></div>
  <div class="abs slider-arrow" style="left:1025px;top:265px;background:var(--blue)"><svg width="8" height="10" viewBox="0 0 8 10" fill="none" stroke="#fff" stroke-width="1.6"><path d="M2 1l4 4-4 4"/></svg></div>
</section>

<!-- FOOTER -->
<footer class="footer">
  <div class="abs" style="left:142px;top:64px">
    <h5>Quick Links</h5>
    <ul>
      <li>- Home</li><li>- About Us</li><li>- Professionals</li><li>- Industries Served</li><li>- Areas Of Practice</li><li>- Resources &amp; Advisories</li>
    </ul>
  </div>
  <div class="abs" style="left:381px;top:64px;width:240px">
    <h5>Contact Details</h5>
    <div class="f-item" style="margin-top:40px"><svg width="12" height="16" viewBox="0 0 12 16" fill="#fff"><path d="M6 0a6 6 0 0 0-6 6c0 4.5 6 10 6 10s6-5.5 6-10a6 6 0 0 0-6-6zm0 8.5A2.5 2.5 0 1 1 6 3.5a2.5 2.5 0 0 1 0 5z"/></svg><div><b>ADDRESS</b>123 Ut Wisi Enim Ad Minim Veniam Quis Nostrud.</div></div>
    <div class="f-item" style="margin-top:14px"><svg width="13" height="13" viewBox="0 0 24 24" fill="#fff"><path d="M6.6 10.8a15 15 0 0 0 6.6 6.6l2.2-2.2a1 1 0 0 1 1-.25 11.4 11.4 0 0 0 3.6.57 1 1 0 0 1 1 1V20a1 1 0 0 1-1 1A17 17 0 0 1 3 4a1 1 0 0 1 1-1h3.5a1 1 0 0 1 1 1c0 1.25.2 2.45.57 3.57a1 1 0 0 1-.25 1z"/></svg><div><b>PHONE</b>123-456-7890</div></div>
    <div class="f-item" style="margin-top:14px"><svg width="13" height="11" viewBox="0 0 24 20" fill="#fff"><path d="M0 0h24v20H0z"/><path d="M1 1l11 9 11-9" stroke="#000" stroke-width="2" fill="none"/></svg><div><b>EMAIL</b>info@harrowgatetrialfirm.com</div></div>
  </div>
  <div class="abs social" style="left:671px;top:64px">
    <h5>Follow Us</h5>
    <ul>
      <li><i></i>Friendwall</li><li><i></i>Viewcast</li><li><i></i>Photoloop</li><li><i></i>Chirpline</li>
    </ul>
  </div>
  <div class="abs f-brand">
    <span class="mark"></span>
    <div class="name">HARROWGATE</div>
    <div class="sub">TRIAL FIRM</div>
  </div>
  <div class="abs copyright">© 2025 HARROWGATE. All Rights Reserved.</div>
</footer>

</body>
</html>
```